Quillory Nest Business Card

I need a business card design. We are a collaborate online training company. Our colors are gray and green. Our website is QuilloryNest.com

I would like an area for a profile picture within the card

```html
<!DOCTYPE html>
<html lang="en">
<head>
<meta charset="utf-8">
<title>Quillory Nest Business Card</title>
<link href="https://fonts.googleapis.com/css2?family=Lato:wght@300;400;700&display=swap" rel="stylesheet">
<style>
  :root {
    --page-bg: #ece9e4;
    --card-white: #ffffff;
    --card-edge: #dcdcdc;
    --brand-green: #7cc243;
    --ink-dark: #2f2f31;
    --ink-mid: #4a4a4c;
    --photo-gray: #3a3b3d;
  }
  * { box-sizing: border-box; margin: 0; padding: 0; }
  html, body {
    width: 1200px;
    height: 1023px;
    overflow: hidden;
    background: var(--page-bg);
    font-family: "Lato", sans-serif;
  }
  .sheet {
    width: 1200px;
    height: 1023px;
    display: flex;
    flex-direction: column;
    align-items: center;
    justify-content: center;
    gap: 60px;
  }
  .card {
    position: relative;
    width: 620px;
    height: 354px;
    background: var(--card-white);
    border: 1px solid var(--card-edge);
    box-shadow: 0 6px 18px rgba(0,0,0,0.12);
    overflow: hidden;
  }
  /* front */
  .card-front .brand {
    position: absolute;
    left: 46px;
    top: 62px;
    display: flex;
    align-items: center;
    gap: 12px;
  }
  .brand-dot {
    width: 30px;
    height: 30px;
    border-radius: 50%;
    background: var(--brand-green);
  }
  .brand-name {
    font-weight: 700;
    font-size: 34px;
    letter-spacing: -0.5px;
    color: var(--ink-dark);
  }
  .person {
    position: absolute;
    left: 46px;
    top: 150px;
  }
  .person-name {
    font-weight: 400;
    font-size: 30px;
    color: var(--ink-dark);
    line-height: 1.1;
  }
  .person-role {
    font-weight: 300;
    font-size: 17px;
    color: var(--ink-mid);
    margin-top: 2px;
  }
  .contact {
    position: absolute;
    left: 46px;
    top: 238px;
    list-style: none;
    font-weight: 300;
    font-size: 16px;
    line-height: 1.55;
    color: var(--ink-mid);
  }
  .photo-panel {
    position: absolute;
    right: 0;
    top: 0;
    width: 230px;
    height: 100%;
  }
  .photo-slot {
    position: absolute;
    left: 14px;
    right: 22px;
    top: 40px;
    bottom: 40px;
    background: linear-gradient(160deg, #ffffff 0%, #f1f1f1 35%, var(--photo-gray) 36%, var(--photo-gray) 100%);
  }
  .panel-stripe {
    position: absolute;
    right: 0;
    top: 0;
    width: 14px;
    height: 100%;
    background: var(--brand-green);
  }
  .panel-tab {
    position: absolute;
    left: 0;
    width: 14px;
    height: 40px;
    background: var(--brand-green);
  }
  .panel-tab.top { top: 0; }
  .panel-tab.bottom { bottom: 0; }
  /* back */
  .card-back {
    display: flex;
    align-items: center;
    justify-content: center;
    gap: 16px;
  }
  .card-back .brand-dot { width: 40px; height: 40px; }
  .card-back .brand-name {
    font-size: 52px;
    color: var(--brand-green);
  }
</style>
</head>
<body>
<main class="sheet">
  <section class="card card-front">
    <div class="brand">
      <span class="brand-dot"></span>
      <span class="brand-name">Quillory Nest</span>
    </div>
    <div class="person">
      <p class="person-name">Marlo Fenwick</p>
      <p class="person-role">Director</p>
    </div>
    <ul class="contact">
      <li>0987 654 321</li>
      <li>marlo@quillorynest</li>
      <li>www.QuilloryNest.com</li>
    </ul>
    <div class="photo-panel">
      <span class="panel-tab top"></span>
      <span class="panel-tab bottom"></span>
      <div class="photo-slot" role="img" aria-label="Profile picture area for the cardholder's portrait"></div>
      <span class="panel-stripe"></span>
    </div>
  </section>

  <section class="card card-back">
    <span class="brand-dot"></span>
    <span class="brand-name">Quillory Nest</span>
  </section>
</main>
</body>
</html>
```